Texting While Driving/Distracted Driving Educational Poster

We are a design-driven nutrition, health, and wellness educational company looking for a fresh, eye-catching educational poster design to promote attentive driving, primarily to young and new drivers. Young, inexperienced drivers (under 20) have the highest proportion of distraction-related fatal crashes, with talking and texting being the most commonly recognized distraction. We hope to draw attention to this issue with an engaging, persuasive poster. The poster will be printed and available for purchase on our website and print catalogs.

Target Market(s)

The audience is American teen to adult drivers and the buyer is educators and healthcare professionals.

Requirements
Must have
• The poster must be 18" x 24" trim size, all fonts in outlines, full color art converted to CMYK.

```html
<!DOCTYPE html>
<html lang="en">
<head>
<meta charset="UTF-8">
<title>Be Smart. Don't Text 'n Drive</title>
<link rel="stylesheet" href="https://fonts.googleapis.com/css2?family=Archivo:wght@600;700;800;900&display=swap">
<style>
  :root {
    --ink: #000000;
    --paper: #ffffff;
    --signal: #f7a600;
    --slang: #333333;
    --rule: #bdbdbd;
  }
  * { margin: 0; padding: 0; box-sizing: border-box; }
  html, body {
    width: 900px;
    height: 1200px;
    overflow: hidden;
    background: var(--ink);
  }
  .poster {
    position: relative;
    width: 900px;
    height: 1200px;
    overflow: hidden;
    background: var(--ink);
    font-family: "Archivo", "Helvetica Neue", Arial, sans-serif;
    color: var(--paper);
  }
  .slang {
    position: absolute;
    left: 12px;
    top: -34px;
    width: 1000px;
    font-weight: 800;
    font-size: 84px;
    line-height: 92px;
    letter-spacing: 1px;
    color: var(--slang);
    white-space: nowrap;
  }
  .headline {
    position: absolute;
    left: 136px;
    top: 370px;
    text-transform: uppercase;
  }
  .headline span { display: block; }
  .headline__lead {
    font-weight: 800;
    font-size: 92px;
    line-height: 92px;
    letter-spacing: 1px;
  }
  .headline__stop {
    margin-top: 2px;
    font-weight: 900;
    font-size: 222px;
    line-height: 196px;
    letter-spacing: -2px;
    color: var(--signal);
  }
  .headline__tail {
    margin-top: 6px;
    font-weight: 800;
    font-size: 76px;
    line-height: 76px;
    letter-spacing: 1px;
  }
  .facts {
    position: absolute;
    left: 140px;
    top: 728px;
    width: 680px;
    height: 350px;
    display: flex;
  }
  .facts__col {
    width: 300px;
    font-weight: 700;
    font-size: 14px;
    line-height: 49px;
    letter-spacing: 0.6px;
    text-transform: uppercase;
    padding-top: 2px;
  }
  .facts__divider {
    width: 1.5px;
    height: 350px;
    margin: 0 34px 0 26px;
    background: var(--rule);
  }
  .facts__col p { margin: 0; }
  .tagline {
    position: absolute;
    left: 0;
    width: 900px;
    top: 1112px;
    text-align: center;
    font-weight: 800;
    font-size: 25px;
    letter-spacing: 0.5px;
    text-transform: uppercase;
  }
</style>
</head>
<body>
  <main class="poster">
    <div class="slang" aria-hidden="true">
      LOL CYA OMG CWOT<br>
      DBEYR DPUP GNBLFY<br>
      LMAO MEH OUSU PMF<br>
      RMMA SYS TLITBC YR
    </div>

    <h1 class="headline">
      <span class="headline__lead">Be Smart.</span>
      <span class="headline__stop">Don’t</span>
      <span class="headline__tail">Text ‘n Drive</span>
    </h1>

    <section class="facts">
      <div class="facts__col">
        <p>Young, inexperienced drivers<br>(under 20) have the highest<br>proportion of distraction-<br>related fatal crashes, with<br>talking and texting being the<br>most commonly recognized.</p>
      </div>
      <div class="facts__divider"></div>
      <div class="facts__col">
        <p>Young, inexperienced drivers<br>(under 20) have the highest<br>proportion of distraction-<br>related fatal crashes, with<br>talking and texting being the<br>most commonly recognized.</p>
      </div>
    </section>

    <p class="tagline">Don’t let distraction steer you into danger!</p>
  </main>
</body>
</html>
```